Life Coach for Lawyers Business Card Design

Elegant, original, business card design for life coaching service for associate attorneys who work in big law and struggle with stress, overwhelm, and time management. Double sided design.

Target Market(s)

Women associate attorneys who work in big law and struggle with stress, overwhelm, and time management.

Industry/Entity Type

Life Coaching

Contact Information for Business Card

Marissa Pendrell
Life Coach
518.677.3941
calmbriefcounsel.net
marissa@calmbriefcounsel.net
@calmbriefcounsel (Instagram)

Font styles to use
Other font styles liked:
• Silver South font duo. See uploaded files.

Requirements
Must have
• Icons for phone, website, email, and Instagram instead of words. Specific colors used in my logo (171B2B, 421121, FFFFFF)
Nice to have
• Foil. Embossed. Feminine design.
Should not have
• Any colors other than those used in logo. See uploaded files.

```html
<!DOCTYPE html>
<html lang="en">
<head>
<meta charset="utf-8">
<title>Calm Brief Counsel – Business Card Back</title>
<link href="https://fonts.googleapis.com/css2?family=Montserrat:wght@300&display=swap" rel="stylesheet">
<style>
  :root {
    --page: #ffffff;
    --navy: #171b2b;
    --gold-line: #e6d72c;
    --white: #ffffff;
  }
  html, body {
    margin: 0;
    padding: 0;
    width: 1200px;
    height: 646px;
    overflow: hidden;
    background: var(--page);
  }
  .canvas {
    width: 1200px;
    height: 646px;
    display: flex;
    align-items: center;
    justify-content: center;
  }
  .card {
    position: relative;
    width: 1000px;
    height: 600px;
    background: var(--navy);
    font-family: "Montserrat", sans-serif;
    color: var(--white);
  }
  .card__frame {
    position: absolute;
    inset: 33px;
    border: 1.5px solid var(--gold-line);
    border-radius: 24px;
  }
  .brand-name {
    position: absolute;
    left: 0;
    right: 0;
    top: 268px;
    margin: 0;
    text-align: center;
    font-weight: 300;
    font-size: 46px;
    letter-spacing: 0.14em;
    text-transform: uppercase;
    line-height: 1;
  }
  .website {
    position: absolute;
    left: 0;
    right: 0;
    top: 458px;
    display: flex;
    align-items: center;
    justify-content: center;
    gap: 10px;
    font-weight: 300;
    font-size: 26px;
    letter-spacing: 0.01em;
  }
  .website__icon {
    width: 30px;
    height: 30px;
  }
</style>
</head>
<body>
  <main class="canvas">
    <section class="card">
      <div class="card__frame"></div>
      <h1 class="brand-name">Calm Brief Counsel</h1>
      <p class="website">
        <svg class="website__icon" viewBox="0 0 24 24" fill="none" stroke="currentColor" stroke-width="1.2" aria-hidden="true">
          <circle cx="12" cy="12" r="10"/>
          <ellipse cx="12" cy="12" rx="4.5" ry="10"/>
          <line x1="2" y1="12" x2="22" y2="12"/>
          <path d="M4 6.5h16M4 17.5h16"/>
        </svg>
        <span>calmbriefcounsel.net</span>
      </p>
    </section>
  </main>
</body>
</html>
```